Webbanner-Design für Gewinnspiel auf Wimbrola
Zielgruppe
Wir starten einmal im Monat auf Wimbrola ein internes Gruppen Gewinnspiel und genau dafür brauchen wir einen Online Flyer.
Aufgabenstellung
Wir suchen einen sehr auffälligen bunten Online Flyer für ein Gewinnspiel auf Wimbrola.
Hier der Text der rein muss.:
Sunny Picks Galore! GEWINNSPIEL
Gewinne jetzt per auslosung einen 250,-€ Gutschein für Korvani.
Regeln:
°Pro 10 eingeladene Mitglieder bekommt ihr 1 Los
°Je mehr Mitglieder ihr einladet , desto mehr Lose und je mehr Lose, desto höher die Gewinnchance
2.Kommentiere unter dem Gewinnspiel wie viele Leute du in die Gruppe eingeladen hast!
3.Sei/Werde ein Gruppenmitglied von Korvani Produkttester und Kinderhilfe.
– Das Gewinnspiel endet am 02.10.2017 + 20:00 Uhr dann findet auch die Live Auslosung statt.
Die Lose werden während des Gewinnspiels jeden Tag um 20:00 Uhr per Quillpost verteilt.
– Der Gewinner wird nach dem Zufallsprinzip ermittelt und via Message verständigt.
(Kleiner Text)–--> Das Gewinnspiel steht in keiner Verbindung zu Wimbrola und wird in keiner Weise von Wimbrola gesponsert, unterstützt oder organisiert. Der Rechtsweg ist ausgeschlossen.
Maße:1x 1200x600 und 1x 600x600
Wie Sie Gestalten und machen ist egal, da wir noch keine konkreten Vorstellungen dazu haben.
Bunt Auffallend und Aussagekräftig sollte der Gewinnspielflyer sein.
Unser Logo sollte auch klein auf dem Flyer zum sehen sein.
Ich habe noch zwei beispiele hochgeladen und solche Grafische Gewinnspielflyer möchten wir auch haben, nur in unserem/ anderen Stil.

```html
<!DOCTYPE html>
<html lang="de">
<head>
<meta charset="utf-8">
<title>Gewinnspiel Flyer – Sunny Picks Galore!</title>
<link href="https://fonts.googleapis.com/css2?family=Antonio:wght@700&family=Oswald:wght@400;500;700&display=swap" rel="stylesheet">
<style>
:root{
  --page:#ffffff;
  --sun-light:#f2fb45;
  --sun-mid:#dbef3c;
  --sun-deep:#b9e232;
  --red:#e8423f;
  --red-warm:#f2573a;
  --sky:#5fb8d4;
  --sky-light:#78cde5;
  --ink:#222222;
  --white:#ffffff;
}
*{box-sizing:border-box;margin:0;padding:0}
html,body{width:1200px;height:598px;overflow:hidden;background:var(--page)}
body{position:relative;font-family:"Oswald",sans-serif;color:var(--ink)}

.banner{position:absolute;overflow:hidden}
.banner--square{left:89px;top:120px;width:300px;height:359px;background:var(--page)}
.banner--wide{left:514px;top:150px;width:600px;height:300px}

.sunburst{position:absolute;background:radial-gradient(circle at 50% 45%,var(--sun-light) 0%,var(--sun-mid) 55%,var(--sun-deep) 100%)}
.banner--square .sunburst{left:0;top:0;width:300px;height:165px}
.banner--wide .sunburst{inset:0;background:radial-gradient(circle at 25% 45%,var(--sun-light) 0%,var(--sun-mid) 55%,var(--sun-deep) 100%)}

.badge{position:absolute;border-radius:50%;background:radial-gradient(circle at 40% 35%,var(--red-warm),var(--red));box-shadow:0 0 0 3px rgba(255,255,120,.6)}
.title{position:absolute;font-family:"Antonio",sans-serif;color:var(--white);font-weight:700;line-height:.95;text-shadow:2px 2px 0 rgba(120,20,20,.45);transform:rotate(-5deg);transform-origin:left top;white-space:nowrap}
.title span{display:block}

.claim{position:absolute;left:0;right:0;text-align:center;color:var(--red);font-weight:500;white-space:nowrap;line-height:1.2}
.prize{position:absolute;color:var(--red);font-weight:500;white-space:nowrap;display:flex;align-items:center}
.prize__tag{background:var(--red);color:var(--white);border-radius:2px;display:inline-flex;align-items:baseline;font-weight:700;overflow:visible}
.prize__tag small{font-weight:500}

.brand{position:absolute;display:flex;align-items:center;gap:3px;color:var(--red);font-weight:500}
.brand__dot{width:7px;height:7px;border-radius:50%;background:var(--red)}

.rules{position:absolute;background:linear-gradient(180deg,var(--sky),var(--sky-light))}
.rules__tab{position:absolute;background:var(--red);color:var(--white);font-weight:500;text-align:center;border-radius:2px 2px 0 0}
.rule{position:absolute;background:var(--white);border-radius:2px;font-size:11px;line-height:13px;padding-left:6px;display:flex;flex-direction:column;justify-content:center;white-space:nowrap}
.rule__num{position:absolute;width:22px;height:22px;border-radius:50%;background:var(--red);color:var(--white);font-weight:700;font-size:15px;line-height:22px;text-align:center;box-shadow:0 0 0 2px var(--white)}

.cta{position:absolute;color:var(--red);font-weight:500;white-space:nowrap;display:flex;align-items:center;gap:4px}
.cta svg{width:10px;height:12px}
.disclaimer{position:absolute;color:var(--ink);white-space:nowrap}

/* square banner */
.banner--square .badge{left:97px;top:8px;width:99px;height:99px}
.banner--square .title{left:91px;top:24px;font-size:23px}
.banner--square .title .title__indent{padding-left:28px}
.banner--square .title .title__big{font-size:30px}
.banner--square .claim{top:111px;font-size:14px}
.banner--square .prize{left:45px;top:132px;font-size:14px;gap:4px}
.banner--square .prize__tag{padding:0 3px;font-size:22px;line-height:25px;gap:2px}
.banner--square .prize__tag small{font-size:13px;line-height:25px}
.banner--square .brand{right:12px;top:18px;font-size:10px}
.banner--square .rules{left:0;top:170px;width:300px;height:189px}
.banner--square .rules__tab{left:31px;top:3px;width:52px;height:18px;font-size:12px;line-height:18px}
.banner--square .cta{left:88px;top:158px;font-size:12px}
.banner--square .disclaimer{left:0;right:0;top:180px;text-align:center;font-size:4.3px}

/* wide banner */
.banner--wide .badge{left:86px;top:58px;width:124px;height:124px}
.banner--wide .title{left:79px;top:78px;font-size:29px}
.banner--wide .title .title__indent{padding-left:34px}
.banner--wide .title .title__big{font-size:37px}
.banner--wide .claim{left:0;right:auto;width:302px;top:186px;font-size:18px}
.banner--wide .prize{left:22px;top:211px;font-size:18px;gap:5px}
.banner--wide .prize__tag{padding:0 4px;font-size:28px;line-height:32px;gap:3px}
.banner--wide .prize__tag small{font-size:16px;line-height:32px}
.banner--wide .brand{right:14px;top:28px;font-size:11px}
.banner--wide .rules{left:298px;top:60px;width:302px;height:178px;border-left:4px solid #bfe7f3}
.banner--wide .rules__tab{left:27px;top:10px;width:51px;height:18px;font-size:12px;line-height:18px}
.banner--wide .cta{left:226px;top:270px;font-size:14px}
.banner--wide .disclaimer{right:10px;top:266px;text-align:right;font-size:5.2px;line-height:7px}
</style>
</head>
<body>

<section class="banner banner--square" aria-label="Gewinnspiel Flyer 600x600">
  <div class="sunburst" role="img" aria-label="Strahlenkranz in Gelbgrün"></div>
  <div class="badge"></div>
  <h1 class="title"><span>Sunny Picks</span><span class="title__indent">Galore!</span><span class="title__big">GEWINNSPIEL</span></h1>
  <p class="claim">Gewinne jetzt per Auslosung</p>
  <p class="prize">einen <span class="prize__tag">€250,–<small>Gutschein</small></span> für Korvani</p>
  <div class="brand"><span class="brand__dot"></span>Herzwerk</div>

  <div class="rules">
    <div class="rules__tab">Regeln</div>
    <div class="rule" style="left:57px;top:15px;width:204px;height:51px">
      <span>Pro 10 eingeladene Mitglieder bekommt ihr 1 Los.</span>
      <span>Je mehr Mitglieder ihr einladet, desto mehr Lose</span>
      <span>und je mehr Lose, desto höher die Gewinnchance</span>
    </div>
    <span class="rule__num" style="left:30px;top:30px">1</span>
    <div class="rule" style="left:57px;top:73px;width:204px;height:36px">
      <span>Kommentiere unter dem Gewinnspiel</span>
      <span>wie viele Leute du in die Gruppe eingeladen hast!</span>
    </div>
    <span class="rule__num" style="left:30px;top:78px">2</span>
    <div class="rule" style="left:57px;top:115px;width:204px;height:36px">
      <span>Sei/Werde ein Gruppenmitglied</span>
      <span>von Korvani Produkttester und Kinderhilfe.</span>
    </div>
    <span class="rule__num" style="left:30px;top:121px">3</span>
    <p class="cta">
      <svg viewBox="0 0 10 12"><path d="M5 0v11M1 7l4 4 4-4" fill="none" stroke="currentColor" stroke-width="1.5"/></svg>
      <span style="color:var(--white)">Hier geht’s zur Gruppe</span>
      <svg viewBox="0 0 10 12"><path d="M5 0v11M1 7l4 4 4-4" fill="none" stroke="currentColor" stroke-width="1.5"/></svg>
    </p>
    <p class="disclaimer">Das Gewinnspiel steht in keiner Verbindung zu Wimbrola und wird in keiner Weise von Wimbrola gesponsert, unterstützt oder organisiert. Der Rechtsweg ist ausgeschlossen.</p>
  </div>
</section>

<section class="banner banner--wide" aria-label="Gewinnspiel Flyer 1200x600">
  <div class="sunburst" role="img" aria-label="Strahlenkranz in Gelbgrün"></div>
  <div class="badge"></div>
  <h1 class="title"><span>Sunny Picks</span><span class="title__indent">Galore!</span><span class="title__big">GEWINNSPIEL</span></h1>
  <p class="claim">Gewinne jetzt per Auslosung</p>
  <p class="prize">einen <span class="prize__tag">€250,–<small>Gutschein</small></span> für Korvani</p>
  <div class="brand"><span class="brand__dot"></span>Herzwerk</div>

  <div class="rules">
    <div class="rules__tab">Regeln</div>
    <div class="rule" style="left:53px;top:22px;width:204px;height:52px">
      <span>Pro 10 eingeladene Mitglieder bekommt ihr 1 Los.</span>
      <span>Je mehr Mitglieder ihr einladet, desto mehr Lose</span>
      <span>und je mehr Lose, desto höher die Gewinnchance</span>
    </div>
    <span class="rule__num" style="left:26px;top:38px">1</span>
    <div class="rule" style="left:53px;top:81px;width:204px;height:36px">
      <span>Kommentiere unter dem Gewinnspiel</span>
      <span>wie viele Leute du in die Gruppe eingeladen hast!</span>
    </div>
    <span class="rule__num" style="left:26px;top:86px">2</span>
    <div class="rule" style="left:53px;top:123px;width:204px;height:36px">
      <span>Sei/Werde ein Gruppenmitglied</span>
      <span>von Korvani Produkttester und Kinderhilfe.</span>
    </div>
    <span class="rule__num" style="left:26px;top:129px">3</span>
  </div>

  <p class="cta">
    <svg viewBox="0 0 10 12"><path d="M5 0v11M1 7l4 4 4-4" fill="none" stroke="var(--white)" stroke-width="1.5"/></svg>
    <span>Hier geht’s zur Gruppe</span>
    <svg viewBox="0 0 10 12"><path d="M5 0v11M1 7l4 4 4-4" fill="none" stroke="var(--white)" stroke-width="1.5"/></svg>
  </p>
  <p class="disclaimer">Das Gewinnspiel steht in keiner Verbindung zu Wimbrola und<br>wird in keiner Weise von Wimbrola gesponsert, unterstützt oder organisiert.<br>Der Rechtsweg ist ausgeschlossen.</p>
</section>

</body>
</html>
```